Halvard Property Website

Our organization has multiple arms. We want a 5-page website to address the divisions of our company. Pelgrave Yards, our 1500 square foot flex office space will have 3 of those pages. We need a landing page for Halvard Property Holdings and a Contact Us page for the organization. Then the 3 pages dedicated to Pelgrave Yards: a page showing office pictures, a page for pricing, and a calendar page for this part of our business; for a total of 5 pages.
Updates

Please note, we need a logo for Pelgrave Yards (the flex office space). We have a logo for Halvard Property (see attachments). It is not a requirement for Pelgrave's logo to match Halvard's logo.

Industry/Entity Type

Real Estate

Coding

Requirements
Must have
• Domain, Email, Logo (for Pelgrave Yards),

```html
<!DOCTYPE html>
<html lang="en">
<head>
<meta charset="utf-8">
<title>Halvard Property – Website Pages</title>
<link href="https://fonts.googleapis.com/css2?family=Cinzel:wght@400;500&family=Roboto:wght@400;500;700&display=swap" rel="stylesheet">
<style>
:root{
  --crimson:#a80c45;
  --pink:#e8306f;
  --pink-soft:#fdeef4;
  --ring:#d77a9f;
  --ink:#1f1f1f;
  --muted:#6b6b6b;
  --line:#e3e3e3;
  --black:#050505;
  --canvas:#ececec;
  --white:#ffffff;
}
*{box-sizing:border-box;margin:0;padding:0}
html,body{width:874px;height:1200px;overflow:hidden;background:var(--canvas)}
body{font-family:'Roboto',sans-serif;color:var(--ink);position:relative}
.page{position:absolute;background:var(--white);overflow:hidden}
.page--home{left:35px;top:36px;width:383px;height:1127px}
.page--contact{left:455px;top:36px;width:384px;height:823px}
.abs{position:absolute}

/* top bar + header */
.topbar{position:absolute;left:0;top:0;width:100%;height:14px;background:var(--crimson);color:var(--white);font-size:4.6px;font-weight:500;text-align:center;line-height:14px;letter-spacing:.1px}
.header{position:absolute;left:0;top:14px;width:100%;height:22px;background:var(--white);z-index:3}
.brand-box{position:absolute;left:35px;top:14px;width:49px;height:43px;background:var(--white);z-index:4;display:flex;flex-direction:column;align-items:center;justify-content:center;gap:4px}
.brand-box .mark{width:10px;height:10px;background:var(--crimson)}
.brand-box .name{font-family:'Cinzel',serif;font-size:7px;color:var(--ink);letter-spacing:.5px}
.nav{position:absolute;top:0;height:22px;font-size:4.4px;font-weight:500;line-height:22px;white-space:nowrap}
.nav.active{color:var(--pink)}
.call{position:absolute;left:285px;top:4px;display:flex;gap:3px;align-items:center}
.call .ico{width:10px;height:10px;border-radius:50%;background:var(--pink);display:flex;align-items:center;justify-content:center}
.call small{display:block;font-size:3.6px;font-weight:700;line-height:5px}
.call b{display:block;font-size:6.6px;color:var(--crimson);font-weight:700;line-height:8px;white-space:nowrap}

/* hero */
.hero-art{position:absolute;left:0;top:0}
.hero-title{position:absolute;color:var(--white);font-family:'Cinzel',serif;line-height:1;white-space:nowrap}
.hero-copy{position:absolute;color:var(--white);font-size:5.3px;font-weight:700;line-height:8.4px}
.dots{position:absolute;display:flex;gap:1.5px}
.dots i{width:3px;height:3px;border-radius:50%;background:var(--white);display:block}
.dots i.off{background:transparent;border:.6px solid var(--white)}

/* buttons */
.btn{position:absolute;height:14px;background:var(--crimson);color:var(--white);font-size:4.4px;font-weight:700;display:flex;align-items:center;justify-content:center;gap:3px;white-space:nowrap;clip-path:polygon(5px 0,100% 0,100% 100%,0 100%)}
.btn::before{content:"";position:absolute;left:0;top:0;width:7px;height:100%;background:var(--pink);clip-path:polygon(5px 0,7px 0,2px 100%,0 100%)}
.btn .arrow{width:4px;height:4px;border-radius:50%;background:var(--white);position:relative}
.btn .arrow::after{content:"";position:absolute;left:1.2px;top:1px;border-left:1.6px solid var(--crimson);border-top:1px solid transparent;border-bottom:1px solid transparent}

.section-title{position:absolute;left:0;width:100%;text-align:center;font-family:'Cinzel',serif;font-weight:400;color:var(--ink)}

/* services */
.service{position:absolute;width:102px;height:78px;overflow:hidden;box-shadow:0 0 2px rgba(0,0,0,.25)}
.service .photo{position:absolute;inset:0}
.service .caption{position:absolute;left:0;bottom:0;width:86px;height:14px;background:var(--white);clip-path:polygon(0 0,74px 0,100% 100%,0 100%);font-size:4.4px;font-weight:500;line-height:14px;padding-left:5px;white-space:nowrap}
.service .caption b{margin-left:4px;font-weight:700}
.service--feature{background:var(--crimson);color:var(--white);text-align:center;padding:12px 7px 0}
.service--feature h4{font-size:5.4px;font-weight:700;margin-bottom:5px}
.service--feature p{font-size:4.3px;line-height:7.2px}
.service--feature .more{margin-top:6px;font-size:4px;font-weight:700;text-decoration:underline}

/* about */
.about{position:absolute;left:0;top:539px;width:383px;height:172px;background:var(--pink-soft);overflow:hidden}
.about h2{position:absolute;left:35px;top:26px;font-family:'Cinzel',serif;font-size:11px;font-weight:400}
.about p{position:absolute;left:35px;top:47px;width:157px;font-size:4.8px;line-height:8.2px;color:var(--muted);text-align:justify}

/* why choose */
.why{position:absolute;width:100px;text-align:center}
.why .ring{width:74px;height:74px;margin:0 auto;border-radius:50%;background:var(--ring);display:flex;align-items:center;justify-content:center}
.why .core{width:63px;height:63px;border-radius:50%;background:var(--crimson);display:flex;align-items:center;justify-content:center}
.why h5{margin-top:12px;font-family:'Cinzel',serif;font-size:5px;font-weight:500;letter-spacing:.2px}
.why p{margin-top:6px;font-size:4.8px;line-height:7.3px;color:var(--muted);text-align:justify;text-align-last:center}

/* footer block */
.site-footer{position:absolute;left:0;width:100%;height:152px;color:var(--white)}
.site-footer h3{position:absolute;left:35px;top:0;font-family:'Cinzel',serif;font-size:8.6px;font-weight:500;letter-spacing:.2px;white-space:nowrap}
.site-footer .sub{position:absolute;left:35px;top:12px;font-size:4.4px;white-space:nowrap}
.signup{position:absolute;left:180px;top:-2px;width:167px;height:15px;display:flex;border:.5px solid #333}
.signup .field{flex:1;background:var(--black);display:flex;align-items:center;gap:3px;padding-left:6px;font-size:4.4px}
.signup .go{width:55px;background:var(--pink);font-size:4.4px;font-weight:700;display:flex;align-items:center;justify-content:center}
.site-footer .rule{position:absolute;left:35px;top:28px;width:312px;height:.5px;background:#333}
.footer-brand{position:absolute;left:35px;top:50px;width:128px;text-align:center;font-family:'Cinzel',serif;font-size:12px;line-height:16px;letter-spacing:1px}
.vline{position:absolute;top:40px;width:.5px;height:74px;background:#333}
.col-title{position:absolute;top:41px;font-family:'Cinzel',serif;font-size:5.6px;letter-spacing:.2px;white-space:nowrap}
.col-title::after{content:"";position:absolute;left:0;top:9px;width:10px;height:1px;background:var(--pink)}
.links{position:absolute;left:186px;top:56px;list-style:none;font-size:4.3px;line-height:8.5px}
.links li::before{content:"+";color:var(--pink);margin-right:5px;font-weight:700}
.contact-item{position:absolute;left:253px;display:flex;gap:5px;align-items:flex-start;white-space:nowrap}
.contact-item .label{color:var(--pink);font-size:3.9px;font-weight:500;display:block}
.contact-item .val{font-size:4.4px;display:block}
.contact-item .val.big{font-size:6px}
.bar{position:absolute;left:0;bottom:0;width:100%;height:15px;background:var(--pink);font-size:4.4px;line-height:15px;padding-left:35px;white-space:nowrap}
.bar .maker{position:absolute;left:301px;top:0;font-family:'Cinzel',serif;font-size:4.6px;letter-spacing:.3px}

/* contact page */
.form-label{position:absolute;font-size:4.6px;font-weight:700;white-space:nowrap}
.input{position:absolute;height:17px;border:.5px solid var(--line);box-shadow:0 0 2px rgba(0,0,0,.08);font-size:4.3px;color:#8a8a8a;padding:0 5px;display:flex;align-items:center;justify-content:space-between}
.input.area{align-items:flex-start;padding-top:6px}
.contact-panel-title{position:absolute;left:35px;top:475px;font-family:'Cinzel',serif;font-size:9px;font-weight:400;color:var(--white)}
.info-row{position:absolute;left:36px;display:flex;gap:6px;align-items:center;color:var(--white);font-size:4.4px;line-height:7.5px;white-space:nowrap}
.info-row .dot{width:11px;height:11px;border-radius:50%;background:var(--white);display:flex;align-items:center;justify-content:center;flex:none}
.map{position:absolute;left:181px;top:474px;width:166px;height:110px;border:2px solid var(--white);background:linear-gradient(135deg,#e4e4e4,#d6d6d6 55%,#e0e0e0)}
</style>
</head>
<body>

<!-- ============ HOME PAGE ============ -->
<div class="page page--home">
  <svg class="hero-art" width="383" height="1127" viewBox="0 0 383 1127">
    <defs>
      <linearGradient id="heroPhoto" x1="0" y1="0" x2="1" y2="1">
        <stop offset="0" stop-color="#8e8f8f"/><stop offset=".45" stop-color="#b3b4b3"/><stop offset="1" stop-color="#84807c"/>
      </linearGradient>
    </defs>
    <g role="img" aria-label="Photo of two colleagues reviewing papers at a desk in a bright office">
      <polygon points="0,36 383,36 383,212 275,272 0,212" fill="url(#heroPhoto)"/>
    </g>
    <polygon points="0,212 275,272 383,212 383,218 275,289 0,228" fill="var(--crimson)"/>
    <polygon points="0,212 275,272 383,212 383,214 275,276 0,218" fill="var(--pink)"/>
    <polygon points="6,970 109,899 383,970 383,976 109,916 0,977" fill="var(--crimson)"/>
    <polygon points="0,977 109,916 383,976 383,1127 0,1127" fill="var(--black)"/>
  </svg>

  <div class="topbar">WELCOME TO HALVARD PROPERTY</div>
  <div class="header">
    <span class="nav active" style="left:119px">Home</span>
    <span class="nav" style="left:141px">About Us</span>
    <span class="nav" style="left:170px">Our Services</span>
    <span class="nav" style="left:206px">Why Choose Us</span>
    <span class="nav" style="left:247px">Contact Us</span>
    <div class="call">
      <span class="ico"><svg width="6" height="6" viewBox="0 0 24 24"><path fill="#fff" d="M6.6 10.8a15 15 0 006.6 6.6l2.2-2.2a1 1 0 011-.25 11.4 11.4 0 003.6.6 1 1 0 011 1V20a1 1 0 01-1 1A17 17 0 013 4a1 1 0 011-1h3.5a1 1 0 011 1c0 1.25.2 2.45.6 3.6a1 1 0 01-.25 1z"/></svg></span>
      <span><small>CALL US TODAY !</small><b>+1 555 014 2290</b></span>
    </div>
  </div>
  <div class="brand-box"><span class="mark"></span><span class="name">HALVARD</span></div>

  <div class="hero-title" style="left:33px;top:98px;font-size:10.5px">WELCOME TO</div>
  <div class="hero-title" style="left:34px;top:116px;font-size:16px">HALVARD PROPERTY</div>
  <p class="hero-copy" style="left:33px;top:139px;width:175px">Lorem ipsum dolor sit amet, consectetur adipiscing elit, sed do eiusmod tempor incididunt ut labore et dolore</p>
  <div class="btn" style="left:35px;top:164px;width:53px">GET STARTED <span class="arrow"></span></div>
  <div class="dots" style="left:183px;top:199px"><i></i><i></i><i class="off"></i><i></i><i></i></div>

  <h2 class="section-title" style="top:293px;font-size:9.5px">OUR SERVICES</h2>

  <div class="service" style="left:34px;top:313px"><div class="photo" role="img" aria-label="Photo of an open office with blue shelving and desks" style="background:linear-gradient(160deg,#c9d0d5,#eef0f1 60%,#bfc4c8)"></div><div class="caption">Lorem ipsum dolor sit amet<b>+</b></div></div>
  <div class="service" style="left:141px;top:313px"><div class="photo" role="img" aria-label="Photo of a team meeting in an industrial style office" style="background:linear-gradient(160deg,#a9aeb2,#dcdedf 55%,#979ca1)"></div><div class="caption">Lorem ipsum dolor sit amet<b>+</b></div></div>
  <div class="service" style="left:248px;top:313px"><div class="photo" role="img" aria-label="Photo of a coworking floor seen from above" style="background:linear-gradient(160deg,#ddd6cf,#f1f1ef 55%,#c2bbb4)"></div><div class="caption">Lorem ipsum dolor sit amet<b>+</b></div></div>
  <div class="service" style="left:34px;top:398px"><div class="photo" role="img" aria-label="Photo of colleagues working at computers" style="background:linear-gradient(160deg,#d3c6b8,#eeebe7 55%,#b8aca0)"></div><div class="caption">Lorem ipsum dolor sit amet<b>+</b></div></div>
  <div class="service service--feature" style="left:141px;top:398px">
    <h4>Lorem ipsum dolor sit amet</h4>
    <p>Sed ut perspiciatis unde omnis iste natus error sit voluptatem accusan doloremque laudantium, totam rem aperiam, eaque ipsa quae ab illo inventore</p>
    <div class="more">LEARN MORE &#10148;</div>
  </div>
  <div class="service" style="left:248px;top:398px"><div class="photo" role="img" aria-label="Photo of an empty office with blue walls and desk rows" style="background:linear-gradient(160deg,#bccbd4,#eaedef 55%,#9ea8b0)"></div><div class="caption">Lorem ipsum dolor sit amet<b>+</b></div></div>

  <div class="btn" style="left:157px;top:497px;width:69px">VIEW ALL SERVICES <span class="arrow"></span></div>

  <section class="about">
    <svg class="abs" style="left:0;top:0" width="383" height="172" viewBox="0 0 383 172">
      <polygon points="232,0 383,0 383,172 187,172" fill="#eceef0" role="img" aria-label="Photo of a team working together around a large office table"/>
      <polygon points="224,0 232,0 187,172 179,172" fill="#c94b7c"/>
    </svg>
    <h2>ABOUT US</h2>
    <p>Sed ut perspiciatis unde omnis iste natus error sit voluptatem accusantium doloremque laudantium, totam rem aperiam, eaque ipsa quae ab illo inventore veritatis et quasi architecto beatae vitae dicta sunt explicabo. Nemo enim ipsam voluptatem quia voluptas sit aspernatur aut odit aut fugit, sed quia consequuntur magni dolores eos qui ratione voluptatem sequi nesciunt. Neque porro quisquam est, qui dolorem ipsum quia dolor sit amet, consectetur, adipisci velit, sed quia non numquam eius modi tempora incidunt ut labore et dolore magnam aliquam quaerat voluptatem.</p>
    <div class="btn" style="left:34px;top:130px;width:52px">GET STARTED <span class="arrow"></span></div>
  </section>

  <h2 class="section-title" style="top:739px;font-size:11px">WHY CHOOSE US</h2>

  <div class="why" style="left:35px;top:766px">
    <div class="ring"><div class="core"><svg width="30" height="30" viewBox="0 0 30 30" fill="none" stroke="#fff" stroke-width="2"><rect x="4" y="3" width="9" height="7" fill="#fff"/><rect x="17" y="3" width="9" height="7" fill="#fff"/><path d="M2 14h26M5 14v13M25 14v13M9 18h5v9M16 18h5v9"/></svg></div></div>
    <h5>LOREM IPSUM DOLOR SIT</h5>
    <p>Lorem ipsum dolor sit amet, consectetur adipiscing elit, sed do eiusmod tempor incididunt ut labore et dolore magna aliqua. Ut enim ad minim veniam,</p>
  </div>
  <div class="why" style="left:141px;top:766px">
    <div class="ring"><div class="core"><svg width="30" height="30" viewBox="0 0 30 30" fill="none" stroke="#fff" stroke-width="2"><path d="M16 4l5 2-2 5M18 5l-6 6"/><rect x="7" y="9" width="7" height="5" fill="#fff"/><path d="M3 15h24M6 15v12h18V15M11 20h8"/></svg></div></div>
    <h5>LOREM IPSUM DOLOR SIT</h5>
    <p>Lorem ipsum dolor sit amet, consectetur adipiscing elit, sed do eiusmod tempor incididunt ut labore et dolore magna aliqua. Ut enim ad minim veniam,</p>
  </div>
  <div class="why" style="left:248px;top:766px">
    <div class="ring"><div class="core"><svg width="30" height="30" viewBox="0 0 30 30" fill="none" stroke="#fff" stroke-width="2"><rect x="5" y="4" width="11" height="8" fill="#fff"/><circle cx="23" cy="6" r="3"/><path d="M3 15h24"/><rect x="6" y="17" width="18" height="10" fill="#fff"/><path d="M6 22h18" stroke="#a80c45"/></svg></div></div>
    <h5>LOREM IPSUM DOLOR SIT</h5>
    <p>Lorem ipsum dolor sit amet, consectetur adipiscing elit, sed do eiusmod tempor incididunt ut labore et dolore magna aliqua. Ut enim ad minim veniam,</p>
  </div>

  <footer class="site-footer" style="top:975px">
    <h3>SUBSCRIBE OUR NEWSLETTER</h3>
    <p class="sub">Lorem ipsum dolor sit amet, consectetur adipiscing elit</p>
    <div class="signup"><span class="field"><svg width="5" height="4" viewBox="0 0 10 8"><rect width="10" height="8" fill="#fff"/><path d="M0 0l5 4 5-4" stroke="#000" fill="none"/></svg>Enter Your Email</span><span class="go">SUBSCRIBE NOW</span></div>
    <div class="rule"></div>
    <div class="footer-brand">HALVARD<br>PROPERTY HOLDINGS</div>
    <div class="vline" style="left:170px"></div>
    <div class="vline" style="left:238px"></div>
    <div class="col-title" style="left:186px">QUICK LINKS</div>
    <ul class="links"><li>Home</li><li>Pricing</li><li>Services</li><li>Our Company</li><li>Blog</li><li>Testimonials</li><li>Contact Us</li></ul>
    <div class="col-title" style="left:253px">CONTACT US</div>
    <div class="contact-item" style="top:67px"><svg width="6" height="9" viewBox="0 0 6 9"><rect x=".5" y=".5" width="5" height="8" rx="1" fill="none" stroke="#fff" stroke-width=".8"/><circle cx="3" cy="7.2" r=".5" fill="#fff"/></svg><span><span class="label">PHONE NO :</span><span class="val big">+1 555 014 2290</span></span></div>
    <div class="contact-item" style="top:86px"><svg width="9" height="7" viewBox="0 0 9 7"><rect x=".4" y=".4" width="8.2" height="6.2" fill="none" stroke="#fff" stroke-width=".8"/><path d="M.4.4l4.1 3.4L8.6.4M.4 6.6l3-2.6M8.6 6.6l-3-2.6" stroke="#fff" stroke-width=".8" fill="none"/></svg><span><span class="label">E MAIL :</span><span class="val">info@halvardproperty.com.au</span></span></div>
    <div class="contact-item" style="top:105px"><svg width="9" height="7" viewBox="0 0 9 7"><rect x=".4" y=".4" width="8.2" height="6.2" fill="none" stroke="#fff" stroke-width=".8"/><path d="M.4.4l4.1 3.4L8.6.4M.4 6.6l3-2.6M8.6 6.6l-3-2.6" stroke="#fff" stroke-width=".8" fill="none"/></svg><span><span class="label">LOCATION :</span><span class="val">147 , Lorem Ipsum Dolor , United States</span></span></div>
    <div class="bar">© 2022 Halvard Property. All Rights Reserved<span class="maker">PELGRAVE YARDS</span></div>
  </footer>
</div>

<!-- ============ CONTACT PAGE ============ -->
<div class="page page--contact">
  <svg class="hero-art" width="384" height="823" viewBox="0 0 384 823">
    <defs>
      <linearGradient id="heroPhoto2" x1="0" y1="0" x2="1" y2="1">
        <stop offset="0" stop-color="#8e8f8f"/><stop offset=".45" stop-color="#b3b4b3"/><stop offset="1" stop-color="#84807c"/>
      </linearGradient>
      <linearGradient id="panelPink" x1="0" y1="0" x2="0" y2="1">
        <stop offset="0" stop-color="#ea3a78"/><stop offset="1" stop-color="#e02a68"/>
      </linearGradient>
    </defs>
    <g role="img" aria-label="Photo of two colleagues reviewing papers at a desk in a bright office">
      <polygon points="0,36 384,36 384,173 275,233 0,173" fill="url(#heroPhoto2)"/>
    </g>
    <polygon points="0,173 275,233 384,173 384,182 275,249 0,188" fill="var(--crimson)"/>
    <polygon points="0,173 275,233 384,173 384,175 275,238 0,178" fill="var(--pink)"/>
    <rect x="0" y="451" width="384" height="230" fill="url(#panelPink)"/>
    <polygon points="0,662 110,596 384,662 384,670 109,610 0,670" fill="var(--crimson)"/>
    <polygon points="0,670 109,610 384,670 384,823 0,823" fill="var(--black)"/>
  </svg>

  <div class="topbar">WELCOME TO HALVARD PROPERTY</div>
  <div class="header">
    <span class="nav" style="left:119px">Home</span>
    <span class="nav" style="left:141px">About Us</span>
    <span class="nav" style="left:170px">Our Services</span>
    <span class="nav" style="left:206px">Why Choose Us</span>
    <span class="nav active" style="left:247px">Contact Us</span>
    <div class="call">
      <span class="ico"><svg width="6" height="6" viewBox="0 0 24 24"><path fill="#fff" d="M6.6 10.8a15 15 0 006.6 6.6l2.2-2.2a1 1 0 011-.25 11.4 11.4 0 003.6.6 1 1 0 011 1V20a1 1 0 01-1 1A17 17 0 013 4a1 1 0 011-1h3.5a1 1 0 011 1c0 1.25.2 2.45.6 3.6a1 1 0 01-.25 1z"/></svg></span>
      <span><small>CALL US TODAY !</small><b>+1 555 014 2290</b></span>
    </div>
  </div>
  <div class="brand-box"><span class="mark"></span><span class="name">HALVARD</span></div>

  <div class="hero-title" style="left:34px;top:100px;font-size:16.5px">CONTACT US</div>
  <div class="dots" style="left:183px;top:199px"><i></i><i></i><i class="off"></i><i></i><i></i></div>

  <h2 class="section-title" style="top:257px;font-size:12px">GET IN TOUCH</h2>

  <span class="form-label" style="left:71px;top:282px">Name</span>
  <span class="form-label" style="left:198px;top:282px">Mobile No</span>
  <div class="input" style="left:66px;top:291px;width:123px">First Name<svg width="4" height="4" viewBox="0 0 8 8"><circle cx="4" cy="2.2" r="2" fill="#555"/><path d="M0 8a4 3.5 0 018 0z" fill="#555"/></svg></div>
  <div class="input" style="left:194px;top:291px;width:122px">Phone No<svg width="4" height="4" viewBox="0 0 24 24"><path fill="#555" d="M6.6 10.8a15 15 0 006.6 6.6l2.2-2.2a1 1 0 011-.25 11.4 11.4 0 003.6.6 1 1 0 011 1V20a1 1 0 01-1 1A17 17 0 013 4a1 1 0 011-1h3.5a1 1 0 011 1c0 1.25.2 2.45.6 3.6a1 1 0 01-.25 1z"/></svg></div>
  <span class="form-label" style="left:71px;top:314px">Email Address</span>
  <div class="input" style="left:66px;top:323px;width:250px">johnsmith@example.com<svg width="5" height="4" viewBox="0 0 10 8"><rect width="10" height="8" fill="#555"/><path d="M0 0l5 4 5-4" stroke="#fff" fill="none"/></svg></div>
  <span class="form-label" style="left:70px;top:347px">Comment or message</span>
  <div class="input area" style="left:66px;top:356px;width:250px;height:48px">What do you talk about ....<svg width="5" height="4" viewBox="0 0 10 8"><ellipse cx="5" cy="3.5" rx="4.4" ry="3" fill="none" stroke="#555"/></svg></div>
  <div class="btn" style="left:165px;top:415px;width:53px">SUBMIT NOW <span class="arrow"></span></div>

  <h3 class="contact-panel-title">CONTACT US</h3>
  <div class="info-row" style="top:496px"><span class="dot"><svg width="6" height="6" viewBox="0 0 10 10"><circle cx="5" cy="5" r="4" fill="none" stroke="#e8306f" stroke-width="1.4"/><path d="M5 2.5V5h2" stroke="#e8306f" stroke-width="1.2" fill="none"/></svg></span><span>Monday - Friday &nbsp;&nbsp;: &nbsp;09.AM - 05.00 PM<br>Saturday - Sunday &nbsp;: &nbsp;Closed</span></div>
  <div class="info-row" style="top:520px"><span class="dot"><svg width="5" height="5" viewBox="0 0 24 24"><path fill="#e8306f" d="M6.6 10.8a15 15 0 006.6 6.6l2.2-2.2a1 1 0 011-.25 11.4 11.4 0 003.6.6 1 1 0 011 1V20a1 1 0 01-1 1A17 17 0 013 4a1 1 0 011-1h3.5a1 1 0 011 1c0 1.25.2 2.45.6 3.6a1 1 0 01-.25 1z"/></svg></span><span style="font-weight:700;font-size:5px">+1 555 014 2290</span></div>
  <div class="info-row" style="top:543px"><span class="dot"><svg width="5" height="4" viewBox="0 0 10 8"><rect width="10" height="8" fill="#e8306f"/><path d="M0 0l5 4 5-4" stroke="#fff" fill="none"/></svg></span><span>info@halvardproperty.com</span></div>
  <div class="info-row" style="top:565px"><span class="dot"><svg width="4" height="6" viewBox="0 0 8 11"><path d="M4 0a4 4 0 00-4 4c0 3 4 7 4 7s4-4 4-7a4 4 0 00-4-4z" fill="#e8306f"/><circle cx="4" cy="4" r="1.4" fill="#fff"/></svg></span><span>147 , Lorem Ipsum Dolor , United States</span></div>
  <div class="map" role="img" aria-label="Map showing the office location"></div>

  <footer class="site-footer" style="top:671px">
    <h3>SUBSCRIBE OUR NEWSLETTER</h3>
    <p class="sub">Lorem ipsum dolor sit amet, consectetur adipiscing elit</p>
    <div class="signup"><span class="field"><svg width="5" height="4" viewBox="0 0 10 8"><rect width="10" height="8" fill="#fff"/><path d="M0 0l5 4 5-4" stroke="#000" fill="none"/></svg>Enter Your Email</span><span class="go">SUBSCRIBE NOW</span></div>
    <div class="rule"></div>
    <div class="footer-brand">HALVARD<br>PROPERTY HOLDINGS</div>
    <div class="vline" style="left:170px"></div>
    <div class="vline" style="left:238px"></div>
    <div class="col-title" style="left:186px">QUICK LINKS</div>
    <ul class="links"><li>Home</li><li>Pricing</li><li>Services</li><li>Our Company</li><li>Blog</li><li>Testimonials</li><li>Contact Us</li></ul>
    <div class="col-title" style="left:253px">CONTACT US</div>
    <div class="contact-item" style="top:67px"><svg width="6" height="9" viewBox="0 0 6 9"><rect x=".5" y=".5" width="5" height="8" rx="1" fill="none" stroke="#fff" stroke-width=".8"/><circle cx="3" cy="7.2" r=".5" fill="#fff"/></svg><span><span class="label">PHONE NO :</span><span class="val big">+1 555 014 2290</span></span></div>
    <div class="contact-item" style="top:86px"><svg width="9" height="7" viewBox="0 0 9 7"><rect x=".4" y=".4" width="8.2" height="6.2" fill="none" stroke="#fff" stroke-width=".8"/><path d="M.4.4l4.1 3.4L8.6.4M.4 6.6l3-2.6M8.6 6.6l-3-2.6" stroke="#fff" stroke-width=".8" fill="none"/></svg><span><span class="label">E MAIL :</span><span class="val">info@halvardproperty.com.au</span></span></div>
    <div class="contact-item" style="top:105px"><svg width="9" height="7" viewBox="0 0 9 7"><rect x=".4" y=".4" width="8.2" height="6.2" fill="none" stroke="#fff" stroke-width=".8"/><path d="M.4.4l4.1 3.4L8.6.4M.4 6.6l3-2.6M8.6 6.6l-3-2.6" stroke="#fff" stroke-width=".8" fill="none"/></svg><span><span class="label">LOCATION :</span><span class="val">147 , Lorem Ipsum Dolor , United States</span></span></div>
    <div class="bar">© 2022 Halvard Property. All Rights Reserved<span class="maker">PELGRAVE YARDS</span></div>
  </footer>
</div>

</body>
</html>
```